Business Card for KV

We need a double sided business card:

First Name Last Name
Cell 987-605-3214
mailbox@pelvaro-post.com

License #8096-WXYZ-2318
WFLMA # 60782
Dunmere County

```html
<!DOCTYPE html>
<html lang="en">
<head>
<meta charset="utf-8">
<title>Kindred Valley — Business Card</title>
<link rel="stylesheet" href="https://fonts.googleapis.com/css2?family=Oswald:wght@400;500;600&display=swap">
<style>
  :root {
    --backdrop: #e4e4e4;
    --navy: #2a4a63;
    --olive: #8a9436;
    --paper: #f4f4f4;
    --white: #ffffff;
  }
  * { margin: 0; padding: 0; box-sizing: border-box; }
  html, body {
    width: 1200px; height: 960px; overflow: hidden;
    background: var(--backdrop);
    font-family: "Oswald", sans-serif;
  }
  .canvas { position: relative; width: 1200px; height: 960px; }

  .card {
    position: absolute; left: 332px; width: 542px; height: 310px;
  }
  .card--front { top: 147px; background: var(--navy); }
  .card--back  { top: 504px; background: var(--paper); }

  .brand {
    position: absolute; left: 0; right: 0;
    display: flex; flex-direction: column; align-items: center;
  }
  .brand__dot { border-radius: 50%; background: var(--olive); }
  .brand__name {
    font-weight: 600; letter-spacing: 0.04em; text-transform: uppercase;
    line-height: 1;
  }

  .card--front .brand { top: 62px; gap: 22px; }
  .card--front .brand__dot { width: 70px; height: 70px; }
  .card--front .brand__name { font-size: 48px; color: var(--white); }

  .card--back .brand { top: 34px; gap: 14px; }
  .card--back .brand__dot { width: 46px; height: 46px; }
  .card--back .brand__name { font-size: 30px; color: var(--navy); }

  .contact {
    position: absolute; top: 201px; left: 0; width: 100%; height: 40px;
  }
  .contact__name {
    position: absolute; right: 288px; top: 8px;
    font-size: 19px; font-weight: 500; color: var(--navy); white-space: nowrap;
  }
  .contact__divider {
    position: absolute; left: 270px; top: 0; width: 1.5px; height: 40px;
    background: var(--olive);
  }
  .contact__list {
    position: absolute; left: 287px; top: 1px; list-style: none;
    font-size: 15px; font-weight: 400; color: var(--navy); line-height: 19px;
  }
  .contact__list li { display: flex; align-items: center; gap: 5px; white-space: nowrap; }
  .contact__list svg { width: 13px; height: 13px; fill: var(--olive); }

  .credentials {
    position: absolute; left: 46px; top: 256px; width: 449px; height: 28px;
    border-top: 1.5px solid var(--olive); border-bottom: 1.5px solid var(--olive);
    display: flex; align-items: center; justify-content: center; gap: 6px;
    font-size: 15px; font-weight: 400; color: var(--navy); white-space: nowrap;
  }
  .credentials__sep { color: var(--olive); }
</style>
</head>
<body>
<main class="canvas">

  <section class="card card--front" aria-label="Card front">
    <div class="brand">
      <span class="brand__dot"></span>
      <span class="brand__name">Kindred Valley</span>
    </div>
  </section>

  <section class="card card--back" aria-label="Card back">
    <div class="brand">
      <span class="brand__dot"></span>
      <span class="brand__name">Kindred Valley</span>
    </div>

    <div class="contact">
      <p class="contact__name">DANIEL OKAFOR</p>
      <span class="contact__divider"></span>
      <ul class="contact__list">
        <li>
          <svg viewBox="0 0 24 24" aria-hidden="true"><path d="M6.6 10.8c1.4 2.8 3.8 5.1 6.6 6.6l2.2-2.2c.3-.3.7-.4 1-.2 1.1.4 2.3.6 3.6.6.6 0 1 .4 1 1V20c0 .6-.4 1-1 1C10.6 21 3 13.4 3 4c0-.6.4-1 1-1h3.5c.6 0 1 .4 1 1 0 1.3.2 2.5.6 3.6.1.3 0 .7-.2 1L6.6 10.8z"/></svg>
          987-605-3214
        </li>
        <li>
          <svg viewBox="0 0 24 24" aria-hidden="true"><path d="M2 5h20v14H2V5zm2 2v.5l8 5 8-5V7H4zm0 2.8V17h16V9.8l-8 5-8-5z"/></svg>
          mailbox@pelvaro-post.com
        </li>
      </ul>
    </div>

    <p class="credentials">
      <span>License #8096-WXYZ-2318</span>
      <span class="credentials__sep">•</span>
      <span>WFLMA # 60782</span>
      <span class="credentials__sep">•</span>
      <span>Dunmere County</span>
    </p>
  </section>

</main>
</body>
</html>
```